Brightwell Plumbers

We need a webpage designed for http://www.brightwellplumbers.example/. Something clean, and focused.

Homepage needs some call to action at the top, also this is a local business so things like telephone, address, ratings, social media, should be present.

We like contact forms above the fold.

http://www.morvanplumbing.example/ is a website that was referenced, although I personally think it looks "old". Something more modern.

http://www.tedsplumbing.example/ has the pieces we like, bit is not visually appealing.

http://kwikhomecareok.example/ is nice looking but doesnt have a good call to action

http://www.nestlyhire.example/ and http://www.theparishpass.example/ is great

Target Market(s)

Adluts, homeowners

Industry/Entity Type

Business

Font styles to use
Sans Serif

Requirements
Must have
• Homepage needs some call to action form at the top, also this is a local business so things like telephone, address, ratings, social media,
Nice to have
• Prefer layouts that have a fixed max width - not that stretch off the screen
Should not have
• don't overdo "plumber theme" - we want professional, clean and uncluttered. No generic pictures of "plumbers" or cartoon plumbers.

```html
<!DOCTYPE html>
<html lang="en">
<head>
<meta charset="utf-8">
<title>Brightwell Plumbing</title>
<link href="https://fonts.googleapis.com/css2?family=Open+Sans:wght@300;400;600&family=Arimo:wght@400;700&display=swap" rel="stylesheet">
<style>
:root{
  --blue:#2f86d6;
  --blue-dark:#2677c4;
  --sky:#1296d9;
  --grey:#666666;
  --ink:#333333;
  --muted:#555555;
  --white:#ffffff;
  --line:#d8d8d8;
  --icon:#222222;
}
*{box-sizing:border-box;margin:0;padding:0}
html,body{width:781px;height:1200px;overflow:hidden;background:var(--white)}
body{position:relative;font-family:"Open Sans",sans-serif;color:var(--ink)}
.abs{position:absolute}

/* header */
.site-header{left:0;top:0;width:781px;height:59px;background:var(--white)}
.brand{font-family:"Arimo",sans-serif;font-weight:700;font-size:18px;color:var(--blue);display:flex;align-items:center;gap:6px;white-space:nowrap}
.brand .dot{width:18px;height:18px;border-radius:50%;background:#555;display:inline-block}
.site-header .brand{left:92px;top:19px}
.call{left:323px;top:20px;font-family:"Arimo",sans-serif;font-weight:700;font-size:16px;color:#555;white-space:nowrap}
.call span{color:var(--blue-dark)}
.btn{background:var(--blue);color:var(--white);border-radius:3px;display:flex;align-items:center;justify-content:center;font-size:9.5px;white-space:nowrap}
.header-btn{left:573px;top:16px;width:124px;height:28px;font-family:"Arimo",sans-serif}

/* hero */
.hero{left:0;top:59px;width:781px;height:315px;background:var(--blue)}
.main-nav{left:0;top:10px;width:781px;font-size:9.5px;color:var(--white)}
.main-nav a{position:absolute;color:var(--white);text-decoration:none;white-space:nowrap}
.hero-photo{left:120px;top:48px;width:426px;height:267px;
  background:
    radial-gradient(ellipse 40% 50% at 78% 30%, rgba(214,170,140,.55) 0%, rgba(214,170,140,0) 70%),
    radial-gradient(ellipse 60% 70% at 50% 70%, #2457b0 0%, rgba(36,87,176,.6) 60%, rgba(47,134,214,0) 100%),
    linear-gradient(180deg, rgba(47,134,214,0) 0%, #2a62b8 45%, #22509e 100%);
  border-radius:120px 140px 0 0}
.contact-form{left:468px;top:71px;width:203px;height:214px;background:var(--white);border-radius:3px;padding:12px 14px;font-family:"Arimo",sans-serif}
.contact-form h3{font-family:"Open Sans",sans-serif;font-weight:400;font-size:11.5px;color:var(--blue);margin:0 0 5px 2px}
.field{border:1px solid var(--line);height:20px;margin-bottom:4px;font-size:8.5px;color:#555;padding:4px 9px}
.field.msg{height:65px;margin-bottom:9px}
.submit{height:19px;font-size:9px;border-radius:2px}

/* why */
.why{left:0;top:374px;width:781px;height:220px;background:var(--grey);color:var(--white)}
.section-title{width:781px;left:0;text-align:center;font-weight:300;font-size:31px;white-space:nowrap}
.why .section-title{top:35px}
.why-text{left:166px;top:91px;width:200px;font-size:9.3px;line-height:11px}
.ticks{left:399px;top:90px;list-style:none;font-size:9.3px;color:#e4e4e4}
.ticks li{display:flex;align-items:center;gap:6px;height:15px;white-space:nowrap}
.why-btn{left:164px;top:157px;width:124px;height:28px}

/* services */
.services{left:0;top:594px;width:781px;height:272px}
.services .section-title{top:37px;color:#333}
.service{width:172px;text-align:center}
.service svg{display:block;margin:0 auto}
.service h4{font-weight:400;font-size:12px;margin-top:20px;color:#333;white-space:nowrap}
.service p{text-align:left;font-size:8.6px;line-height:10.2px;color:var(--muted);margin-top:13px}

/* dealer */
.dealer{left:0;top:866px;width:781px;height:270px;background:var(--sky);color:var(--white)}
.dealer-text{left:0;top:31px;width:781px;text-align:center;font-size:12.5px;line-height:14px}
.video{left:259px;top:91px;width:273px;height:153px;background:#111}
.video-bar{height:14px;font-size:6px;color:#ddd;padding:3px 6px;white-space:nowrap}
.video-frame{height:124px;background:radial-gradient(ellipse at 50% 45%,#49a6e4 0%,#1a6fb8 60%,#0e4a86 100%);display:flex;align-items:center;justify-content:center}
.video-frame p{font-size:13px;line-height:15px;color:var(--white);margin-left:40px}
.video-controls{height:15px;background:#1b1b1b;border-top:2px solid #444}

/* footer */
.site-footer{left:0;top:1136px;width:781px;height:64px}
.site-footer .brand{left:90px;top:24px}
.foot-nav{left:297px;top:32px;font-family:"Arimo",sans-serif;font-size:8px;color:#222;display:flex;gap:6px}
.badge{background:#2a5fa0}
.social{width:18px;height:18px;border-radius:50%;background:#333;top:27px}
</style>
</head>
<body>

<header class="abs site-header">
  <div class="abs brand"><span class="dot"></span>Brightwell Plumbing</div>
  <div class="abs call">Call Today <span>555-014-2077</span></div>
  <div class="abs btn header-btn">Request a service today!</div>
</header>

<section class="abs hero">
  <nav class="abs main-nav">
    <a style="left:178px">HOME</a>
    <a style="left:238px">OUR SERVICES</a>
    <a style="left:333px">TESTIMONIALS</a>
    <a style="left:428px">ABOUT US</a>
    <a style="left:506px">FAQ</a>
    <a style="left:557px">CONTACT US</a>
  </nav>
  <div class="abs hero-photo" role="img" aria-label="Team of four smiling plumbers in blue work overalls holding tools"></div>
  <form class="abs contact-form">
    <h3>Send us an email</h3>
    <div class="field">Name</div>
    <div class="field">Phone Number</div>
    <div class="field">Email</div>
    <div class="field msg">How can we help you?</div>
    <div class="btn submit">Submit</div>
  </form>
</section>

<section class="abs why">
  <h2 class="abs section-title">Why Choose Brightwell Plumbing</h2>
  <p class="abs why-text">Plumbers with a Service Area from Burbank to Ontario, all of Orange County,From Seal Beach to Laguna Beach, Anaheim and Corona, All Points In-Between</p>
  <ul class="abs ticks">
    <li><svg width="9" height="8" viewBox="0 0 9 8"><path d="M1 4.5l2.3 2.3L8 1.5" stroke="#e4e4e4" stroke-width="1.8" fill="none"/></svg>You approve the price before we start work.</li>
    <li><svg width="9" height="8" viewBox="0 0 9 8"><path d="M1 4.5l2.3 2.3L8 1.5" stroke="#e4e4e4" stroke-width="1.8" fill="none"/></svg>Always FREE work estimates.</li>
    <li><svg width="9" height="8" viewBox="0 0 9 8"><path d="M1 4.5l2.3 2.3L8 1.5" stroke="#e4e4e4" stroke-width="1.8" fill="none"/></svg>Same-day service generally available.</li>
    <li><svg width="9" height="8" viewBox="0 0 9 8"><path d="M1 4.5l2.3 2.3L8 1.5" stroke="#e4e4e4" stroke-width="1.8" fill="none"/></svg>Call today to find out how we can help!</li>
  </ul>
  <div class="abs btn why-btn">request a service today!</div>
</section>

<section class="abs services">
  <h2 class="abs section-title">Brightwell Plumbing Services</h2>
  <div class="abs service" style="left:86px;top:108px">
    <svg width="36" height="42" viewBox="0 0 36 42"><rect x="14" y="0" width="8" height="5" fill="var(--icon)"/><circle cx="20" cy="22" r="14" fill="var(--icon)"/><circle cx="20" cy="22" r="7" fill="#fff"/><rect x="16" y="21" width="8" height="2" fill="var(--icon)"/><rect x="1" y="16" width="6" height="12" fill="var(--icon)"/><rect x="14" y="36" width="12" height="6" fill="var(--icon)"/></svg>
    <h4>Trenchless Sewer Repair</h4>
    <p>Brightwell Plumbers of Los Angeles has a complete system that allows us to repair your broken sewer pipe line all the way to the city sewer line in the street.</p>
  </div>
  <div class="abs service" style="left:298px;top:108px;width:184px">
    <svg width="42" height="42" viewBox="0 0 42 42"><rect x="4" y="0" width="12" height="4" fill="var(--icon)"/><path d="M7 4v22a10 10 0 0 0 20 0v-6h8" stroke="var(--icon)" stroke-width="6" fill="none"/><rect x="34" y="14" width="5" height="12" fill="var(--icon)"/></svg>
    <h4>Copper &amp; PEX Tubing Repipes</h4>
    <p>If your water flow has slowed to a dribble then whole house copper repiping might be just what you need.</p>
  </div>
  <div class="abs service" style="left:514px;top:108px">
    <svg width="42" height="42" viewBox="0 0 42 42"><rect x="2" y="8" width="30" height="26" rx="3" fill="var(--icon)"/><path d="M32 14l8-4v22l-8-4z" fill="var(--icon)"/><rect x="10" y="16" width="14" height="10" fill="#fff"/><rect x="13" y="19" width="8" height="4" fill="var(--icon)"/></svg>
    <h4>Video Pipe Inspection</h4>
    <p>Brightwell Plumbers has a complete pipe camera and plumbing camera system that allows us to see video inside your pipes.</p>
  </div>
</section>

<section class="abs dealer">
  <p class="abs dealer-text">Brightwell Plumbers is the Sole Authorized Dealer and Installer for<br>Clearbrook Water Systems in Orange County, Riverside and<br>San Bernardino Counties, and San Gabriel Valley, Southeast Los Angeles.</p>
  <div class="abs video">
    <div class="video-bar">Safeguarding your water with the Clearbrook Water Systems Combo Series</div>
    <div class="video-frame" role="img" aria-label="Video still of rippling blue water"><p>Sparkling, Clean Water<br>for You and Your Family</p></div>
    <div class="video-controls"></div>
  </div>
</section>

<footer class="abs site-footer">
  <div class="abs brand"><span class="dot"></span>Brightwell Plumbing</div>
  <nav class="abs foot-nav"><span>Home</span><span>Services</span><span>Testimonials</span><span>About</span><span>FAQ</span><span>Contact</span></nav>
  <div class="abs badge" style="left:530px;top:22px;width:16px;height:30px"></div>
  <div class="abs badge" style="left:558px;top:22px;width:34px;height:30px;border-radius:50%"></div>
  <div class="abs social" style="left:598px"></div>
  <div class="abs social" style="left:622px"></div>
  <div class="abs social" style="left:646px"></div>
  <div class="abs social" style="left:669px"></div>
</footer>

</body>
</html>
```